Conflict prevention NGO needs business cards ASAP

We are a small NGO based in New Caledonia working on conflict prevention, and will be attending a WCA-sponsored conference on small arms next month. Our work involves campaigning against the proliferation of small arms in this post-conflict South Pacific island, and we need business cards to match that purpose.
Our three basic guidelines are the following:
1. We would like the logo of our organisation (see attached) included on this card. We are open to a redesign of this logo to something more stylised or abstract.
2. The card would need to be double-sided: one side in French, the other in English. The text should ideally be minimalist, uncluttered, clear and concise. We prefer the card to visually communicate our mission. As such, we would like the card to present a central image or logo, which would give us the option of printing a texture onto that image/logo later.
3. I have attached images which might inspire the designer (bullets and the famous knotted gun statue). However, these are NOT prescriptive; they are simply thematic ideas, and designers should use their own creative license. We only ask that the overall business card communicate professionalism and a seriousness of purpose, rather than sentimentalism or idealism.
Thanks to everyone who is willing to offer up a design idea! I am grateful for your time, and look forward to viewing your ideas. I apologise, but this has to be a rush job. Please get in touch if you need further guidance.
Please note that our new website will go live on Wednesday evening (Brisbane time), in case it can provide inspiration: http://www.lagonclair.org/
Business
ENGLISH SIDE
[Name, Position] Tomas Verhalen, Director
[Organisation] The Centre for a Bright Lagoon
[Sub-Title] The first New Caledonian think tank
[Tel] +61497215304
[Email] centrelagonclair@mailvero.net
[Website] http://www.lagonclair.org/
FRENCH SIDE
[Name, Position] Tomas Verhalen, Directeur
[Organisation] Le Centre pour le Lagon Clair
[Sub-Title] Le premier pôle de réflexion calédonien
[Tel] +61497215304
*Note: We are flexible on the exact way you present the above information, and you may wish to use icons instead of "Tel." for example.

```html
<!DOCTYPE html>
<html lang="en">
<head>
<meta charset="utf-8">
<title>Centre for a Bright Lagoon – Business Cards</title>
<link href="https://fonts.googleapis.com/css2?family=Open+Sans:wght@400;600;700&display=swap" rel="stylesheet">
<style>
  :root {
    --backdrop: #8c7458;
    --card-blue: #0a7fc4;
    --card-white: #ffffff;
    --line-blue: #3d8fd6;
    --ink-dark: #1c1c1c;
    --ink-white: #ffffff;
    --accent-yellow: #f2e21a;
    --accent-blue: #2a86d4;
    --icon-yellow: #e9d92a;
  }
  * { box-sizing: border-box; margin: 0; padding: 0; }
  html, body {
    width: 1200px; height: 1023px; overflow: hidden;
    background: var(--backdrop);
    font-family: "Open Sans", Arial, sans-serif;
  }
  .stage { position: relative; width: 1200px; height: 1023px; }
  .card {
    position: absolute; width: 700px; height: 400px;
    box-shadow: 0 10px 24px rgba(0,0,0,.35);
    overflow: hidden;
  }
  .card--english { left: 70px; top: 60px; background: var(--card-blue); color: var(--ink-white); }
  .card--french { left: 430px; top: 560px; background: var(--card-white); color: var(--ink-dark); }

  .emblem {
    position: absolute; display: flex; align-items: center; gap: 10px;
  }
  .emblem__square {
    width: 74px; height: 74px; background: var(--card-white);
    border: 3px solid var(--accent-blue);
  }
  .card--english .emblem__square { border-color: var(--card-white); }
  .emblem__name { font-size: 13px; font-weight: 700; }

  .card--english .emblem { left: 40px; top: 40px; }
  .card--french .emblem { right: 40px; top: 36px; }

  .org { position: absolute; line-height: 1.3; }
  .org__name { font-size: 20px; font-weight: 700; }
  .org__sub { font-size: 17px; font-weight: 400; }
  .card--english .org { left: 40px; top: 136px; }
  .card--french .org { left: 40px; top: 40px; }

  .knotted-arm {
    position: absolute; border-radius: 6px;
  }
  .card--english .knotted-arm {
    left: 300px; top: 150px; width: 210px; height: 220px;
    background: linear-gradient(160deg, rgba(255,255,255,.10), rgba(255,255,255,.04));
  }
  .card--french .knotted-arm {
    left: 380px; top: 130px; width: 290px; height: 170px;
    background: linear-gradient(160deg, #eef5fc, #dbe9f7);
  }

  .person { position: absolute; }
  .person__name { font-size: 22px; font-weight: 700; }
  .person__role { font-size: 17px; }
  .card--english .person { right: 40px; top: 40px; text-align: right; }
  .card--english .person__role { color: var(--accent-yellow); }
  .card--french .person { left: 40px; top: 200px; }
  .card--french .person__role { color: var(--accent-blue); }

  .contacts { position: absolute; list-style: none; font-size: 17px; line-height: 1.55; }
  .card--english .contacts { right: 40px; bottom: 36px; text-align: right; }
  .card--french .contacts { left: 40px; bottom: 30px; }
  .contacts li { display: flex; align-items: center; gap: 10px; }
  .card--english .contacts li { justify-content: flex-end; }
  .contacts svg { width: 16px; height: 16px; flex: none; }
</style>
</head>
<body>
<main class="stage">

  <section class="card card--english" aria-label="English side">
    <div class="emblem">
      <div class="emblem__square"></div>
      <span class="emblem__name">Bright Lagoon</span>
    </div>
    <div class="org">
      <p class="org__name">The Centre for a Bright Lagoon</p>
      <p class="org__sub">New Caledonian ThinkTank</p>
      <p class="org__sub">Conflict Prevention Reconciliation</p>
    </div>
    <div class="knotted-arm" role="img" aria-label="Faint line drawing of a revolver with its barrel tied in a knot"></div>
    <div class="person">
      <p class="person__name">Tomas Verhalen</p>
      <p class="person__role">Director</p>
    </div>
    <ul class="contacts">
      <li>+61497215304
        <svg viewBox="0 0 16 16"><path d="M4 1l3 3-2 2c1 2 3 4 5 5l2-2 3 3-2 3C7 15 1 9 1 3z" fill="var(--icon-yellow)"/></svg></li>
      <li>centrelagonclair@mailvero.net
        <svg viewBox="0 0 16 16"><rect x="1" y="3" width="14" height="10" fill="var(--icon-yellow)"/><path d="M1 3l7 6 7-6" stroke="var(--card-blue)" fill="none"/></svg></li>
      <li>www.lagonclair.org
        <svg viewBox="0 0 16 16"><circle cx="8" cy="8" r="7" fill="var(--icon-yellow)"/><path d="M1 8h14M8 1v14M3 4h10M3 12h10" stroke="var(--card-blue)" fill="none"/></svg></li>
    </ul>
  </section>

  <section class="card card--french" aria-label="French side">
    <div class="org">
      <p class="org__name">Arms Control · Le Centre pour le Lagon Clair</p>
      <p class="org__sub">Pôle de Réflexion Calédonien · Prévention</p>
      <p class="org__sub">des Conflits Réconciliation Contrôle des Armements</p>
    </div>
    <div class="emblem">
      <div class="emblem__square"></div>
    </div>
    <div class="knotted-arm" role="img" aria-label="Line drawing of a revolver with its barrel tied in a knot"></div>
    <div class="person">
      <p class="person__name">Tomas Verhalen</p>
      <p class="person__role">Directeur</p>
    </div>
    <ul class="contacts">
      <li><svg viewBox="0 0 16 16"><path d="M4 1l3 3-2 2c1 2 3 4 5 5l2-2 3 3-2 3C7 15 1 9 1 3z" fill="var(--accent-blue)"/></svg>+61497215304</li>
      <li><svg viewBox="0 0 16 16"><rect x="1" y="3" width="14" height="10" fill="var(--accent-blue)"/><path d="M1 3l7 6 7-6" stroke="#fff" fill="none"/></svg>centrelagonclair@mailvero.net</li>
      <li><svg viewBox="0 0 16 16"><circle cx="8" cy="8" r="7" fill="var(--accent-blue)"/><path d="M1 8h14M8 1v14M3 4h10M3 12h10" stroke="#fff" fill="none"/></svg>www.lagonclair.org</li>
    </ul>
  </section>

</main>
</body>
</html>
```